Need business cards for our e-assessment business

We need professional looking business cards for our e-assessment business based in Europe. Our company is called Velmora.

You can just use sample name and addresses.

The colours we use are:

#70abe4 (blue)
#FF6600 (orange)

The back side should say: E-assessment made easy

This is the print-shop we are using. Please look at the link for info about formats: http://nl.pribbly-print.com/help/faq/using-my-own-artwork.html

Target Market(s)

Target market is education and large corporations

Industry/Entity Type

Business

```html
<!DOCTYPE html>
<html lang="en">
<head>
<meta charset="utf-8">
<title>Velmora business cards</title>
<link rel="stylesheet" href="https://fonts.googleapis.com/css2?family=Mulish:ital,wght@0,400;0,700;0,800;1,800&display=swap">
<style>
  :root {
    --page: #ebeceb;
    --white: #ffffff;
    --orange: #ef781f;
    --blue: #88b4e2;
    --ink: #3f3f40;
    --soft: #fde3cf;
  }
  * { box-sizing: border-box; margin: 0; padding: 0; }
  html, body { width: 944px; height: 1200px; overflow: hidden; background: var(--page); }
  body { position: relative; font-family: "Mulish", "Century Gothic", sans-serif; }

  .card {
    position: absolute;
    left: 136px;
    width: 644px;
    height: 432px;
    box-shadow: 0 6px 16px rgba(0,0,0,0.28);
  }
  .card--front { top: 134px; }
  .card--back { top: 635px; }
  .card__bg { position: absolute; inset: 0; display: block; }

  .brand { position: absolute; display: flex; align-items: center; gap: 36px; }
  .card--front .brand { left: 116px; top: 42px; }
  .card--back .brand { left: 121px; top: 53px; }
  .brand__dot { width: 120px; height: 120px; border-radius: 50%; background: var(--orange); }
  .brand__name { font-size: 66px; font-weight: 400; color: var(--ink); letter-spacing: -0.5px; line-height: 1; }

  .person { position: absolute; left: 83px; top: 314px; color: var(--white); }
  .person__name { font-size: 22px; font-weight: 800; line-height: 1.2; }
  .person__role { font-size: 19px; font-weight: 400; color: var(--soft); line-height: 1.3; }

  .contacts { position: absolute; left: 281px; top: 272px; list-style: none; }
  .contacts li { display: flex; align-items: center; height: 31px; color: var(--white); font-size: 18px; font-weight: 800; }
  .contacts svg { width: 20px; height: 20px; margin-right: 15px; fill: none; stroke: var(--white); stroke-width: 1.6; }

  .tagline {
    position: absolute; left: 0; right: 0; top: 298px;
    text-align: center; color: var(--white);
    font-size: 37px; font-weight: 800; font-style: italic;
  }
</style>
</head>
<body>

<section class="card card--front">
  <svg class="card__bg" viewBox="0 0 644 432" aria-hidden="true">
    <rect width="644" height="432" fill="var(--white)"/>
    <path d="M0 215 H644 V231 H99 V272 L47 231 H0 Z" fill="var(--blue)"/>
    <path d="M0 236 H40 L103 284 V236 H644 V432 H0 Z" fill="var(--orange)"/>
  </svg>
  <div class="brand">
    <span class="brand__dot"></span>
    <span class="brand__name">velmora</span>
  </div>
  <div class="person">
    <p class="person__name">Your Name</p>
    <p class="person__role">Position</p>
  </div>
  <ul class="contacts">
    <li><svg viewBox="0 0 20 20"><path d="M6 3 L8 7 L6.5 9 C7.5 11.5 9 13 11 14 L13 12.5 L17 14.5 L15.5 17.5 C9 17 3.5 11.5 3 5 Z"/></svg>123-456-7890</li>
    <li><svg viewBox="0 0 20 20"><rect x="5.5" y="2.5" width="9" height="15" rx="1.5"/><line x1="8.5" y1="15" x2="11.5" y2="15"/></svg>123-456-7888</li>
    <li><svg viewBox="0 0 20 20"><rect x="2.5" y="5" width="15" height="10"/><path d="M2.5 5 L10 11 L17.5 5"/></svg>name@velmora.com.eu</li>
    <li><svg viewBox="0 0 20 20"><circle cx="10" cy="10" r="7.5"/><ellipse cx="10" cy="10" rx="3.5" ry="7.5"/><line x1="2.5" y1="10" x2="17.5" y2="10"/><line x1="10" y1="2.5" x2="10" y2="17.5"/></svg>www.velmora.com.eu</li>
  </ul>
</section>

<section class="card card--back">
  <svg class="card__bg" viewBox="0 0 644 432" aria-hidden="true">
    <rect width="644" height="432" fill="var(--white)"/>
    <path d="M0 215 H644 V231 H598 L546 272 V231 H0 Z" fill="var(--blue)"/>
    <path d="M0 236 H541 V284 L604 236 H644 V432 H0 Z" fill="var(--orange)"/>
  </svg>
  <div class="brand">
    <span class="brand__dot"></span>
    <span class="brand__name">velmora</span>
  </div>
  <p class="tagline">E-assessment made easy</p>
</section>

</body>
</html>
```